Automotive Accessories Business Card

Design a business template that match our new logo design and our industry.

https://www.kelvramotive.com/

Target Market(s)

Aftermarket auto parts and accessories

Industry/Entity Type

automotive

Contact Information for Business Card

company logo

Font styles to use
Serif
Sans Serif

Colors
EB3D1F
EC4F4E
F09395
F8D3D4
FCEDEE

```html
<!DOCTYPE html>
<html lang="en">
<head>
<meta charset="utf-8">
<title>Kelvra Motive Inc — Business Card</title>
<link rel="stylesheet" href="https://fonts.googleapis.com/css2?family=Montserrat:wght@700;800&family=Open+Sans:ital,wght@0,400;0,600;1,700&display=swap">
<style>
  :root {
    --brand-red: #EB3D1F;
    --accent-red: #E23A44;
    --ink: #3a3a3c;
    --ink-soft: #4a4a4d;
    --paper: #f7f7f7;
    --paper-edge: #e9e9ea;
    --charcoal-1: #2b2b2d;
    --charcoal-2: #3c3c3f;
    --charcoal-3: #1c1c1e;
    --stage: #ececec;
    --white: #ffffff;
  }
  * { box-sizing: border-box; margin: 0; padding: 0; }
  html, body { width: 1200px; height: 960px; overflow: hidden; }
  body {
    background: var(--stage);
    display: flex;
    flex-direction: column;
    align-items: center;
    justify-content: center;
    gap: 30px;
    font-family: "Open Sans", sans-serif;
  }
  .card {
    position: relative;
    width: 770px;
    height: 440px;
    border-radius: 4px;
    overflow: hidden;
    box-shadow: 0 10px 28px rgba(0,0,0,.18);
  }

  /* Front */
  .card--front {
    background: linear-gradient(135deg, var(--white) 0%, var(--paper) 55%, var(--paper-edge) 100%);
    color: var(--ink);
  }
  .brand {
    position: absolute;
    display: flex;
    align-items: center;
    gap: 14px;
    white-space: nowrap;
  }
  .card--front .brand { left: 150px; top: 70px; }
  .brand__mark {
    width: 26px;
    height: 26px;
    background: var(--accent-red);
    flex: none;
  }
  .brand__name {
    font-family: "Montserrat", sans-serif;
    font-weight: 800;
    font-size: 40px;
    letter-spacing: 1px;
    color: var(--accent-red);
  }
  .divider-bar {
    position: absolute;
    left: 230px;
    top: 160px;
    width: 480px;
    height: 12px;
    background: var(--ink);
  }
  .contacts {
    position: absolute;
    left: 60px;
    top: 200px;
    list-style: none;
    font-size: 19px;
    line-height: 36px;
    color: var(--ink-soft);
  }
  .contacts__item { display: flex; align-items: center; gap: 12px; white-space: nowrap; }
  .contacts__icon { width: 18px; height: 18px; flex: none; }
  .contacts__domain { color: var(--accent-red); font-weight: 700; font-style: italic; }
  .person {
    position: absolute;
    right: 60px;
    top: 280px;
    text-align: right;
  }
  .person__name {
    font-family: "Montserrat", sans-serif;
    font-weight: 800;
    font-size: 34px;
    letter-spacing: 1.5px;
    color: var(--ink);
    white-space: nowrap;
  }
  .person__role {
    margin-top: 2px;
    font-size: 21px;
    color: var(--ink-soft);
  }

  /* Back */
  .card--back {
    background: linear-gradient(135deg, var(--charcoal-2) 0%, var(--charcoal-1) 50%, var(--charcoal-3) 100%);
  }
  .card__facets { position: absolute; inset: 0; width: 100%; height: 100%; }
  .card--back .brand {
    left: 50%;
    top: 50%;
    transform: translate(-50%, -50%);
  }
  .card--back .brand__mark { background: var(--white); }
  .card--back .brand__name { color: var(--white); font-size: 48px; }
</style>
</head>
<body>

  <section class="card card--front" aria-label="Business card front">
    <div class="brand">
      <span class="brand__mark"></span>
      <span class="brand__name">KELVRA MOTIVE INC</span>
    </div>

    <div class="divider-bar"></div>

    <ul class="contacts">
      <li class="contacts__item">
        <svg class="contacts__icon" viewBox="0 0 24 24" aria-hidden="true"><path fill="#E23A44" d="M6.6 10.8a15.1 15.1 0 0 0 6.6 6.6l2.2-2.2a1 1 0 0 1 1-.25 11.4 11.4 0 0 0 3.6.57 1 1 0 0 1 1 1V20a1 1 0 0 1-1 1A17 17 0 0 1 3 4a1 1 0 0 1 1-1h3.5a1 1 0 0 1 1 1c0 1.25.2 2.45.57 3.57a1 1 0 0 1-.25 1z"/></svg>
        <span>1-866-555-0148</span>
      </li>
      <li class="contacts__item">
        <svg class="contacts__icon" viewBox="0 0 24 24" aria-hidden="true"><rect x="2" y="5" width="20" height="14" fill="#E23A44"/><path d="M2 5l10 8 10-8" fill="none" stroke="#fff" stroke-width="1.6"/></svg>
        <span>sales@kelvramotive.com</span>
      </li>
      <li class="contacts__item">
        <svg class="contacts__icon" viewBox="0 0 24 24" aria-hidden="true"><circle cx="12" cy="12" r="10" fill="#E23A44"/><path d="M2 12h20M12 2c3 3 3 17 0 20M12 2c-3 3-3 17 0 20" fill="none" stroke="#fff" stroke-width="1.3"/></svg>
        <span>www.<span class="contacts__domain">kelvramotive</span>.com</span>
      </li>
    </ul>

    <div class="person">
      <p class="person__name">MARCUS DELANE</p>
      <p class="person__role">Sales Manager</p>
    </div>
  </section>

  <section class="card card--back" aria-label="Business card back">
    <svg class="card__facets" viewBox="0 0 770 440" preserveAspectRatio="none" aria-hidden="true">
      <polygon points="0,0 520,0 0,330" fill="#ffffff" opacity="0.06"/>
      <polygon points="330,440 640,60 770,60 770,440" fill="#000000" opacity="0.18"/>
      <polygon points="430,440 600,190 640,440" fill="#ffffff" opacity="0.04"/>
    </svg>
    <div class="brand">
      <span class="brand__mark"></span>
      <span class="brand__name">KELVRA MOTIVE INC</span>
    </div>
  </section>

</body>
</html>
```